Graphic Design for Ledgerwave Forum Event

We are looking for up to 15 hi-tech image designs for use in advertising our cryptocurrency/blockchain event (www.ledgerwaveforum.example) online. Designs to be 1200 x 628

We will be using these images for online advertising of our summit and preference will be given to those with eye catching and clean designs.

Target Market(s)

Corporate CEO’s, CTO’s & CIO’s
Managing Director’s & VP’s
Blockchain Startups
Social Entrepreneurs
Technology Futurists
Attorney’s & Securities Lawyers
Blockchain Developers
FinTech Execs
ICO Advisors/Consultant’s
VC’s/Investors

Industry/Entity Type

Information Technology

Font styles to use
Sans Serif

Colors

Designer to choose colors to be used in the design.

Requirements
Must have
• Eye catching designs relating to the blockchain and cryptocurrency industries
Nice to have
• Suggested copy for ads would be nice
Should not have
• Please keep focused on industry.

```html
<!DOCTYPE html>
<html lang="en">
<head>
<meta charset="utf-8">
<title>Ledgerwave Forum – Event Banner</title>
<link rel="stylesheet" href="https://fonts.googleapis.com/css2?family=Poppins:wght@600&family=Roboto:wght@300;400;500&display=swap">
<style>
  :root {
    --orange: #f26b21;
    --orange-deep: #ee5a24;
    --amber: #f7a823;
    --title: #f05a28;
    --navy: #030a1a;
    --net-blue: #1e6fd9;
    --ink-soft: #6b6b6b;
    --rule: #f26b21;
    --white: #ffffff;
  }
  * { margin: 0; padding: 0; box-sizing: border-box; }
  html, body { width: 1200px; height: 628px; overflow: hidden; background: var(--white); }
  .banner {
    position: relative; width: 1200px; height: 628px; overflow: hidden;
    background: var(--white);
    font-family: "Roboto", Arial, sans-serif;
  }
  .banner-shapes { position: absolute; inset: 0; }

  .brand {
    position: absolute; top: 44px; right: 22px;
    display: flex; align-items: center; gap: 8px;
    font-family: "Roboto", Arial, sans-serif; font-weight: 500; font-size: 13px;
    color: var(--ink-soft);
  }
  .brand-dot { width: 18px; height: 18px; border-radius: 50%; background: var(--ink-soft); }

  .event-meta {
    position: absolute; top: 114px; left: 636px; width: 510px;
    display: flex; justify-content: space-between; align-items: center;
    font-weight: 400; font-size: 19px; letter-spacing: 3.6px; color: var(--orange-deep);
  }
  .meta-item { display: flex; align-items: center; gap: 22px; }
  .meta-item svg { flex: none; }

  .event-title {
    position: absolute; top: 152px; left: 583px; width: 600px; text-align: center;
    font-family: "Poppins", Arial, sans-serif; font-weight: 600; font-size: 50px;
    letter-spacing: -0.5px; color: var(--title); line-height: 1.2;
  }
  .event-tagline {
    position: absolute; top: 230px; left: 583px; width: 600px; text-align: center;
    font-weight: 300; font-size: 27px; color: var(--orange-deep);
  }

  .speaker-rail { position: absolute; top: 310px; left: 676px; width: 426px; height: 50px; }

  .speakers {
    position: absolute; top: 370px; left: 583px; width: 620px;
    display: flex; justify-content: space-between;
  }
  .speaker { width: 206px; text-align: center; }
  .speaker-photo {
    width: 130px; height: 130px; border-radius: 50%; margin: 0 auto 16px;
    background: radial-gradient(circle at 50% 40%, #d9d4cf, #b9b4ae 70%, #e9e7e4);
  }
  .speaker-photo.dark { background: radial-gradient(circle at 50% 40%, #4b4e55, #2a2c31 75%); }
  .speaker-name {
    font-weight: 500; font-size: 14px; letter-spacing: 1.6px; text-transform: uppercase;
    color: var(--orange-deep);
  }
  .speaker-role { margin-top: 14px; font-size: 11px; color: var(--ink-soft); }
</style>
</head>
<body>
<main class="banner">
  <svg class="banner-shapes" width="1200" height="628" viewBox="0 0 1200 628" aria-hidden="false">
    <defs>
      <radialGradient id="netGlow" cx="30%" cy="40%" r="75%">
        <stop offset="0" stop-color="#0d3b7a"/>
        <stop offset="0.55" stop-color="#061a3d"/>
        <stop offset="1" stop-color="#030a1a"/>
      </radialGradient>
    </defs>
    <rect class="network-art" x="0" y="0" width="660" height="628" fill="url(#netGlow)"
          role="img" aria-label="Glowing blue blockchain network of connected nodes on a dark background"/>
    <polygon class="accent-band" fill="var(--orange)"
             points="590,0 642,0 478,352 578,578 1200,578 1200,628 312,628"/>
    <polygon class="accent-wedge" fill="var(--amber)" points="312,628 432,372 548,628"/>
    <polygon class="content-panel" fill="var(--white)" points="642,0 1200,0 1200,578 578,578 478,352"/>
  </svg>

  <div class="brand"><span class="brand-dot"></span>Ledgerwave Forum</div>

  <div class="event-meta">
    <span class="meta-item">
      <svg width="18" height="18" viewBox="0 0 18 18" fill="none" stroke="var(--orange-deep)" stroke-width="2">
        <rect x="1.5" y="3" width="15" height="13.5" rx="1"/><line x1="1.5" y1="7" x2="16.5" y2="7"/>
        <line x1="5" y1="1" x2="5" y2="4"/><line x1="13" y1="1" x2="13" y2="4"/>
      </svg>
      28/29 MARCH 2018
    </span>
    <span class="meta-item">
      <svg width="16" height="20" viewBox="0 0 16 20"><path d="M8 0C3.6 0 0 3.5 0 7.8 0 13.5 8 20 8 20s8-6.5 8-12.2C16 3.5 12.4 0 8 0z" fill="var(--orange-deep)"/><circle cx="8" cy="7.6" r="3" fill="#fff"/></svg>
      TAMPA,FL
    </span>
  </div>

  <h1 class="event-title">Ledgerwave Forum</h1>
  <p class="event-tagline">Bringing Thought Leaders To You</p>

  <svg class="speaker-rail" width="426" height="50" viewBox="0 0 426 50" fill="none" stroke="var(--rule)" stroke-width="1.5">
    <polyline points="7,48 7,19 195,19"/>
    <polyline points="231,19 419,19 419,48"/>
    <rect x="207" y="1" width="12" height="22" rx="6" fill="var(--rule)" stroke="none"/>
    <path d="M201,17 a12,12 0 0 0 24,0" stroke-width="2"/>
    <line x1="213" y1="29" x2="213" y2="36" stroke-width="2"/>
  </svg>

  <section class="speakers">
    <article class="speaker">
      <div class="speaker-photo" role="img" aria-label="Portrait photo of speaker Kenji Arakawa"></div>
      <h2 class="speaker-name">Kenji Arakawa</h2>
      <p class="speaker-role">ICO Advisor &amp; Investor</p>
    </article>
    <article class="speaker">
      <div class="speaker-photo" role="img" aria-label="Portrait photo of speaker Elena Marchetti"></div>
      <h2 class="speaker-name">Elena Marchetti, Ph.D.</h2>
      <p class="speaker-role">CEO of Northvale Capital Group</p>
    </article>
    <article class="speaker">
      <div class="speaker-photo dark" role="img" aria-label="Portrait photo of speaker Lian Qiao"></div>
      <h2 class="speaker-name">Lian Qiao</h2>
      <p class="speaker-role">Fin Tech Thought Leader</p>
    </article>
  </section>
</main>
</body>
</html>
```